Firmen Logo und Visitenkarte mit Terminkarte (Rückseite der Visitenkarte)
Zielgruppe
Feinklar ist ein Kosmetik Institut. Zu den angebotenen Dienstleistungen gehören Kosmetik- und Wellness-Behandlungen.
Aufgabenstellung
Entwerfen Sie bitte ein Logo für meine Internetseite, sowie für eine Visitenkarte mit Terminkarte, die modern, exklusiv und hochwertig strukturiert ist.
Auf der Visitenkarte sollte das Logo stehen: feinklar, Kosmetik, Wellness, Ihr nächster Termin: Freies Feld zum eintragen von Datum und Uhrzeit, Sollten sie Ihren Termin nicht einhalten können, bitte ich Sie diesen 24 Stunden vorher abzusagen. Sowie die Adresse.
Kosmetikerin/Krankenschwester

```html
<!DOCTYPE html>
<html lang="de">
<head>
<meta charset="utf-8">
<title>Feinklar – Logo, Visitenkarte und Terminkarte</title>
<link href="https://fonts.googleapis.com/css2?family=Questrial&family=Poppins:ital,wght@0,600;1,600&display=swap" rel="stylesheet">
<style>
  :root {
    --berry: #93206e;
    --grey: #8a8a8a;
    --line: #c9c9c9;
    --paper: #ffffff;
    --sans: "Questrial", sans-serif;
    --accent: "Poppins", sans-serif;
  }
  * { box-sizing: border-box; margin: 0; padding: 0; }
  html, body { width: 984px; height: 1200px; overflow: hidden; background: var(--paper); }
  body { position: relative; font-family: var(--sans); }

  .brand { position: absolute; top: 215px; left: 0; width: 984px; text-align: center; }
  .brand__name { color: var(--berry); font-size: 104px; line-height: 1; letter-spacing: 2px; }
  .brand__claim { margin-top: 10px; color: var(--grey); font-size: 31px; letter-spacing: 2px; }

  .card { position: absolute; left: 297px; width: 390px; height: 258px; background: var(--paper); border: 1px solid #eee; overflow: hidden; }
  .card__wave { position: absolute; inset: 0; }
  .card--front { top: 478px; }
  .card--back { top: 790px; }

  .front__logo { position: absolute; right: 30px; top: 24px; text-align: center; }
  .front__name { color: var(--berry); font-size: 40px; line-height: 1; }
  .front__claim { color: var(--grey); font-size: 14px; letter-spacing: 1px; margin-top: 6px; }

  .front__person { position: absolute; left: 30px; top: 142px; color: #fff; font-size: 12.5px; line-height: 1.35; white-space: nowrap; }
  .front__person strong { font-family: var(--accent); font-weight: 600; font-size: 12.5px; }
  .front__address { margin-top: 14px; }
  .front__contact { position: absolute; left: 198px; top: 172px; color: #fff; font-size: 12px; line-height: 1.5; list-style: none; white-space: nowrap; }
  .front__contact li { display: flex; align-items: center; gap: 8px; }
  .front__contact svg { width: 12px; height: 12px; flex: none; }

  .back__title { position: absolute; top: 14px; left: 0; width: 100%; text-align: center; font-family: var(--accent); font-style: italic; font-weight: 600; color: var(--berry); font-size: 17px; }
  .schedule { position: absolute; top: 46px; left: 24px; right: 24px; display: grid; grid-template-columns: repeat(3, 1fr); column-gap: 18px; }
  .schedule__head { color: var(--grey); font-size: 13px; height: 24px; }
  .schedule__slot { border-bottom: 1px solid var(--grey); height: 29px; }
  .back__note { position: absolute; left: 22px; bottom: 10px; color: #fff; font-style: italic; font-size: 12px; line-height: 1.3; white-space: nowrap; }
</style>
</head>
<body>

<header class="brand">
  <div class="brand__name">feinklar</div>
  <div class="brand__claim">kosmetik • wellness</div>
</header>

<section class="card card--front" aria-label="Visitenkarte Vorderseite">
  <svg class="card__wave" viewBox="0 0 390 258" preserveAspectRatio="none" aria-hidden="true">
    <path d="M0 96 C70 76 130 91 205 116 C275 141 335 136 390 124" fill="none" stroke="var(--line)" stroke-width="2"/>
    <path d="M0 102 C70 82 130 97 205 122 C275 147 335 142 390 130 L390 258 L0 258 Z" fill="var(--berry)"/>
  </svg>
  <div class="front__logo">
    <div class="front__name">feinklar</div>
    <div class="front__claim">kosmetik • wellness</div>
  </div>
  <div class="front__person">
    <strong>Marlene Vossberg</strong><br>
    Kosmetikerin<br>
    Krankenschwester
    <div class="front__address">Lindenweg 12<br>57072 Birkental</div>
  </div>
  <ul class="front__contact">
    <li><svg viewBox="0 0 12 12"><path d="M1 5 Q6 1 11 5 L10 6.5 L8 5.5 L8 4.5 Q6 3.8 4 4.5 L4 5.5 L2 6.5 Z M3 7 H9 L10 11 H2 Z" fill="#fff"/></svg>02731 / 556274</li>
    <li><svg viewBox="0 0 12 12"><rect x="0.5" y="2" width="11" height="8" fill="none" stroke="#fff"/><path d="M0.5 2 L6 7 L11.5 2" fill="none" stroke="#fff"/></svg>studio@feinklar.example</li>
    <li><svg viewBox="0 0 12 12"><rect x="2.5" y="0.5" width="7" height="11" rx="3.5" fill="#fff"/><path d="M6 1 V5 M2.5 5 H9.5" stroke="var(--berry)"/></svg>feinklar.example</li>
  </ul>
</section>

<section class="card card--back" aria-label="Terminkarte Rückseite">
  <svg class="card__wave" viewBox="0 0 390 258" preserveAspectRatio="none" aria-hidden="true">
    <path d="M0 206 C80 186 150 194 225 200 C295 206 345 200 390 186" fill="none" stroke="var(--line)" stroke-width="2"/>
    <path d="M0 212 C80 192 150 200 225 206 C295 212 345 206 390 192 L390 258 L0 258 Z" fill="var(--berry)"/>
  </svg>
  <h2 class="back__title">Ihre nächsten Wohlfül-Termine:</h2>
  <div class="schedule">
    <div class="schedule__head">Wochentag</div>
    <div class="schedule__head">Datum</div>
    <div class="schedule__head">Uhrzeit</div>
    <div class="schedule__slot"></div><div class="schedule__slot"></div><div class="schedule__slot"></div>
    <div class="schedule__slot"></div><div class="schedule__slot"></div><div class="schedule__slot"></div>
    <div class="schedule__slot"></div><div class="schedule__slot"></div><div class="schedule__slot"></div>
    <div class="schedule__slot"></div><div class="schedule__slot"></div><div class="schedule__slot"></div>
  </div>
  <p class="back__note">Im Verhinderungsfall<br>bitte mindestens 24 Stunden im Voraus abmelden.</p>
</section>

</body>
</html>
```